Non-profit wants to save the world needs Wordpress presence

My name is Tomas Verdugo. I'm a photographer who started a charity (Rancho las Brumas) to help the rural schools and health clinics in Central America. We distribute schools supplies and help health clinics with much needed medical supplies and equipment. I need a way to accept donations. I need to have several different writers post to the blog (in Spanish and English). I have a domain name registered (www.rancholasbrumas.org) and started a simple wordpress site as well at http://www.rancholasbrumas.blogsite.com

Industry/Entity Type

Charity

```html
<!DOCTYPE html>
<html lang="en">
<head>
<meta charset="utf-8">
<title>Rancho las Brumas</title>
<link href="https://fonts.googleapis.com/css2?family=Source+Sans+3:wght@400;600;700&family=Oswald:wght@400&display=swap" rel="stylesheet">
<style>
:root{
  --page:#ebebea;
  --teal:#64a6b0;
  --teal-dark:#4b939b;
  --accent:#f0532b;
  --navy:#1d3280;
  --ink:#3c3c3c;
  --muted:#777;
  --link:#5aa2ad;
  --panel:#f5f5f4;
  --footer-bar:#444;
  --footer-text:#e4f1f2;
}
*{margin:0;padding:0;box-sizing:border-box}
html,body{width:703px;height:1200px;overflow:hidden}
body{background:var(--page);font-family:"Source Sans 3",sans-serif;color:var(--ink);position:relative}
.abs{position:absolute}

.brand{left:60px;top:9px;width:72px;font-family:"Oswald",sans-serif;font-size:15px;line-height:18px;color:var(--navy)}
.donate{left:454px;top:17px;width:62px;height:40px;background:var(--accent);color:#fff;border-radius:3px;font-weight:700;font-size:12.5px;line-height:13px;text-align:center;padding-top:6px;box-shadow:0 5px 6px -3px rgba(0,0,0,.35)}
.search{left:524px;top:27px;width:120px;height:19px;background:#fafafa;border:1px solid #cfcfcf;border-radius:3px;font-size:7px;font-style:italic;color:#666;padding:4px 7px}
.search svg{position:absolute;right:6px;top:3px}

.nav{left:58px;top:72px;width:585px;height:26px;background:var(--teal);border-radius:3px}
.nav a{position:absolute;top:7px;color:#fff;font-weight:600;font-size:10.5px;text-decoration:none}
.nav .current{left:88px;top:-3px;width:42px;height:26px;background:var(--accent);text-align:center;padding-top:10px}

.slider{left:58px;top:110px;width:585px;height:214px;background:linear-gradient(180deg,#4f6a3a 0%,#7d8a5a 45%,#8b7a62 75%,#6f6a50 100%)}
.arrow{top:207px;width:28px;height:28px;border-radius:50%;background:rgba(230,230,230,.6)}
.dots{left:332px;top:308px;width:40px;height:11px;background:#fff;border-radius:2px;display:flex;gap:2px;justify-content:center;align-items:center}
.dots i{width:5px;height:5px;border-radius:50%;background:#555}
.dots i.on{background:var(--accent)}
.slider-shadow{left:90px;top:334px;width:520px;height:14px;background:radial-gradient(ellipse at center top,rgba(0,0,0,.2),transparent 70%)}

.section-title{font-size:13.5px;font-weight:600;letter-spacing:.3px;color:#333}
.latest-title{left:60px;top:366px}
.latest-rule{left:58px;top:391px;width:378px;height:4px;border-top:1px solid #c8c8c8;border-bottom:1px solid #c8c8c8}

.post{left:58px;width:378px;height:146px;border-bottom:1px solid #d4d4d4}
.post .thumb{position:absolute;left:5px;top:0;width:133px;height:91px;border:3px solid #fff;box-shadow:0 1px 3px rgba(0,0,0,.2)}
.post h3{position:absolute;left:156px;top:0;width:222px;font-size:13px;font-weight:600;line-height:16px;color:#444}
.post .meta{position:absolute;left:156px;top:36px;font-size:7px;color:var(--link)}
.post .share{position:absolute;left:299px;top:34px;display:flex;gap:5px}
.post .share i{width:12px;height:12px;border-radius:50%;background:#666}
.post p{position:absolute;left:156px;top:53px;width:200px;font-size:6.2px;line-height:9.6px;color:#666}

.widget{left:476px;width:166px;background:var(--panel);border:2px solid #fff;border-radius:3px;box-shadow:0 1px 2px rgba(0,0,0,.12)}
.widget-shadow{left:486px;width:146px;height:14px;background:radial-gradient(ellipse at center top,rgba(0,0,0,.22),transparent 70%)}
.widget h4{font-size:13.5px;font-weight:600;color:#333;letter-spacing:.3px}
.older ul{list-style:none;margin-top:9px}
.older li{font-size:6px;color:#888;line-height:16px;padding-left:20px;position:relative}
.older li::before{content:"»";position:absolute;left:8px;top:-1px;font-size:10px;color:var(--teal-dark)}
.email{margin:12px auto 0;width:136px;height:26px;border:2px solid #cfcfcf;border-radius:3px;background:#f3f3f3;font-size:7px;font-style:italic;color:#666;padding:7px 10px}
.submit{margin:18px auto 0;width:82px;height:24px;background:var(--teal);color:#fff;font-weight:600;font-size:10.5px;text-align:center;line-height:24px}
.video{margin:10px auto 0;width:80px;height:51px;border:2px solid #444;background:linear-gradient(135deg,#2a3326,#556048 60%,#8b8a72);position:relative}
.video svg{position:absolute;left:22px;top:8px}

.footer{left:0;top:1009px;width:703px;height:165px;background:var(--teal-dark);color:var(--footer-text)}
.footer h5{position:absolute;font-size:16px;font-weight:600;color:#fff}
.footer ul{position:absolute;list-style:none}
.footer li{font-size:10.5px;font-weight:600;line-height:16.8px}
.footer .tags{position:absolute;left:358px;top:50px;width:120px;font-size:10.5px;font-weight:600;line-height:17.6px}
.follow li{display:flex;align-items:center;gap:9px;line-height:17.6px}
.follow i{width:11px;height:11px;display:block}
.copyright{left:0;top:1174px;width:703px;height:26px;background:var(--footer-bar);color:#ddd;font-size:7px;text-align:center;line-height:26px}
</style>
</head>
<body>
<div class="abs brand">Rancho las Brumas</div>
<div class="abs donate">Donate<br>Now!</div>
<div class="abs search">Search post
  <svg width="12" height="12" viewBox="0 0 12 12"><circle cx="4.8" cy="4.8" r="3.5" fill="none" stroke="#3d7f8a" stroke-width="1.6"/><line x1="7.4" y1="7.4" x2="11" y2="11" stroke="#3d7f8a" stroke-width="2"/></svg>
</div>

<nav class="abs nav">
  <a class="current" href="#">Home</a>
  <a href="#" style="left:139px">About Us</a>
  <a href="#" style="left:201px">Our Projects</a>
  <a href="#" style="left:280px">Blogs</a>
  <a href="#" style="left:324px">News</a>
  <a href="#" style="left:369px">Support Us</a>
  <a href="#" style="left:441px">Contact Us</a>
</nav>

<div class="abs slider" role="img" aria-label="Photo of children on a rural village path with a photographer kneeling to take their picture"></div>
<div class="abs arrow" style="left:62px"><svg width="28" height="28" viewBox="0 0 28 28"><path d="M16 8 L10 14 L16 20" fill="none" stroke="#555" stroke-width="3"/></svg></div>
<div class="abs arrow" style="left:611px"><svg width="28" height="28" viewBox="0 0 28 28"><path d="M12 8 L18 14 L12 20" fill="none" stroke="#555" stroke-width="3"/></svg></div>
<div class="abs dots"><i></i><i class="on"></i><i></i><i></i></div>
<div class="abs slider-shadow"></div>

<h2 class="abs section-title latest-title">LATEST POSTS</h2>
<div class="abs latest-rule"></div>

<article class="abs post" style="top:407px">
  <div class="thumb" role="img" aria-label="Photo of a boy standing by a wooden fence and green tarp" style="background:linear-gradient(135deg,#5a4a30,#8a7550 45%,#2f8a5a 70%,#9a8460)"></div>
  <h3>Lorem ipsum dolor sit amet, consect etur adipisicing elit...</h3>
  <div class="meta">September 24 &nbsp; • &nbsp; 14 Comments</div>
  <div class="share"><i></i><i></i><i></i></div>
  <p>Lorem ipsum dolor sit amet, consectetur adipisicing elit, sed do eiusmod tempor incididunt ut labore et dolore magna aliqua. Ut enim ad minim veniam, quis nostrud exercitation ullamco laboris nisi ut aliquip ex ea commodo consequat. Duis aute irure dolor in.</p>
</article>
<article class="abs post" style="top:553px">
  <div class="thumb" role="img" aria-label="Photo of two smiling girls in front of a brick wall" style="background:linear-gradient(135deg,#9aa59a,#b89a80 50%,#5f8f6a)"></div>
  <h3>Lorem ipsum dolor sit amet, consect etur adipisicing elit...</h3>
  <div class="meta">September 24 &nbsp; • &nbsp; 14 Comments</div>
  <div class="share"><i></i><i></i><i></i></div>
  <p>Lorem ipsum dolor sit amet, consectetur adipisicing elit, sed do eiusmod tempor incididunt ut labore et dolore magna aliqua. Ut enim ad minim veniam, quis nostrud exercitation ullamco laboris nisi ut aliquip ex ea commodo consequat. Duis aute irure dolor in.</p>
</article>
<article class="abs post" style="top:699px">
  <div class="thumb" role="img" aria-label="Photo of children and adults walking along a village path" style="background:linear-gradient(180deg,#4f6a3a,#7d8a5a 50%,#8b7a62)"></div>
  <h3>Lorem ipsum dolor sit amet, consect etur adipisicing elit...</h3>
  <div class="meta">September 24 &nbsp; • &nbsp; 14 Comments</div>
  <div class="share"><i></i><i></i><i></i></div>
  <p>Lorem ipsum dolor sit amet, consectetur adipisicing elit, sed do eiusmod tempor incididunt ut labore et dolore magna aliqua. Ut enim ad minim veniam, quis nostrud exercitation ullamco laboris nisi ut aliquip ex ea commodo consequat. Duis aute irure dolor in.</p>
</article>
<article class="abs post" style="top:845px">
  <div class="thumb" role="img" aria-label="Photo of a boy standing beside a green tarp in a yard" style="background:linear-gradient(135deg,#2f8a5a,#6a5a3a 45%,#a08a60)"></div>
  <h3>Lorem ipsum dolor sit amet, consect etur adipisicing elit...</h3>
  <div class="meta">September 24 &nbsp; • &nbsp; 14 Comments</div>
  <div class="share"><i></i><i></i><i></i></div>
  <p>Lorem ipsum dolor sit amet, consectetur adipisicing elit, sed do eiusmod tempor incididunt ut labore et dolore magna aliqua. Ut enim ad minim veniam, quis nostrud exercitation ullamco laboris nisi ut aliquip ex ea commodo consequat. Duis aute irure dolor in.</p>
</article>

<aside class="abs widget older" style="top:370px;height:174px;padding:8px 8px">
  <h4>OLDER POSTS</h4>
  <ul>
    <li>Lorem ipsum dolor sit amet,</li>
    <li>Consectetur adipisicing elit, sed do</li>
    <li>Eiusmod tempor incididunt ut</li>
    <li>Labore et dolore magna aliqua. Ut</li>
    <li>Enim ad minim veniam, quis</li>
    <li>Nostrud exercitation ullamco</li>
    <li>Maboris nisi ut aliquip ex ea</li>
    <li>Yommodo consequat. Duis aute</li>
  </ul>
</aside>
<div class="abs widget-shadow" style="top:546px"></div>

<aside class="abs widget" style="top:588px;height:124px;padding:10px 6px">
  <h4>NEWSLETTER SIGN UP</h4>
  <div class="email">Enter your Email</div>
  <div class="submit">Submit</div>
</aside>
<div class="abs widget-shadow" style="top:714px"></div>

<aside class="abs widget" style="top:760px;height:174px;padding:12px 0;text-align:center">
  <h4>WATCH OUR VIDEOS</h4>
  <div class="video" role="img" aria-label="Video thumbnail"><svg width="32" height="32" viewBox="0 0 32 32"><circle cx="16" cy="16" r="14" fill="rgba(0,0,0,.25)" stroke="#fff" stroke-width="2"/><path d="M12 9 L23 16 L12 23Z" fill="#fff"/></svg></div>
  <div class="video" role="img" aria-label="Video thumbnail" style="margin-top:14px"><svg width="32" height="32" viewBox="0 0 32 32"><circle cx="16" cy="16" r="14" fill="rgba(0,0,0,.25)" stroke="#fff" stroke-width="2"/><path d="M12 9 L23 16 L12 23Z" fill="#fff"/></svg></div>
</aside>
<div class="abs widget-shadow" style="top:936px"></div>

<footer class="abs footer">
  <h5 style="left:92px;top:14px">Quick Links</h5>
  <ul style="left:110px;top:42px">
    <li>Home</li><li>About Us</li><li>Our Projects</li><li>Blogs</li><li>News</li><li>Support Us</li><li>Contact Us</li>
  </ul>
  <h5 style="left:240px;top:14px">Archives</h5>
  <ul style="left:243px;top:42px">
    <li>January (6)</li><li>February (9)</li><li>March (4)</li><li>April (4)</li><li>June (5)</li><li>July (7)</li><li>August (8)</li>
  </ul>
  <h5 style="left:390px;top:14px">Tags</h5>
  <div class="tags">News, dolor sit amet, consectetur, BLOGS, adipisicing elit, sed do eiusmod, tempor, Donation, ut labore et</div>
  <h5 style="left:506px;top:14px">Follow Us</h5>
  <ul class="follow" style="left:512px;top:46px">
    <li><i style="background:#3b5998"></i>Townsquare</li>
    <li><i style="background:#1da1f2"></i>Chirpline</li>
    <li><i style="background:#dd4b39"></i>Searchwell</li>
    <li><i style="background:#c4161c"></i>Clipstream</li>
    <li><i style="background:#f26522"></i>Rss</li>
  </ul>
</footer>
<div class="abs copyright">Copyright@rancholasbrumas.2014.All Rights Reserved.</div>
</body>
</html>
```